Business Card / Email signature with new logo
New logo for Real estate Agent
Business Card / Email signature with new logo - Real Estate
Creative Brief
Professional
Lena Vortham
Realtor
4817 Bellgrove Lane, Ste. 300 Allen, TX 75098
Lena@LenaVorthamRealty.example
www.LenaVorthamRealty.example
License #0382741
I am looking for something that compliments my new logo.. I like the logo in the black background but have sent both for utilization. Ijust want a nice appealing card.
I would like to see the logo as one side of the card and the information on the back. I need to have the Dunmore Pike logo on the card as well on the back and it needs to be noted that : Each Dunmore Pike Office is Independently owned & Operated. I would also like to have the Realtor and HPX symbol included on the the card.

```html
<!DOCTYPE html>
<html lang="en">
<head>
<meta charset="utf-8">
<title>Lena Vortham Realty – Business Card</title>
<link href="https://fonts.googleapis.com/css2?family=Tinos:wght@400;700&display=swap" rel="stylesheet">
<style>
  :root {
    --backdrop: #e7e4e0;
    --card: #ffffff;
    --ink: #3b3b3b;
    --muted: #6b6b6b;
    --brand-red: #c8262c;
    --band: #474747;
    --gold: #c9a560;
    --badge: #8a8a8a;
  }
  * { box-sizing: border-box; margin: 0; padding: 0; }
  html, body { width: 1200px; height: 564px; overflow: hidden; }
  body {
    background: var(--backdrop);
    font-family: "Tinos", "Times New Roman", serif;
    color: var(--ink);
    position: relative;
  }
  .card {
    position: absolute;
    top: 114px;
    width: 532px;
    height: 336px;
    background: var(--card);
    box-shadow: 0 6px 18px rgba(0,0,0,0.22);
    overflow: hidden;
  }
  .card--front { left: 44px; }
  .card--back { left: 624px; }

  .brand {
    display: flex;
    align-items: center;
    gap: 10px;
    font-weight: 700;
    color: var(--ink);
    line-height: 1;
  }
  .brand__mark {
    width: 14px; height: 14px;
    background: var(--gold);
    border-radius: 50%;
    flex: none;
  }
  .card--front .brand {
    position: absolute; left: 24px; top: 46px;
    font-size: 27px;
  }
  .agent {
    position: absolute; left: 384px; top: 24px;
  }
  .agent__name { color: var(--brand-red); font-size: 18px; font-weight: 700; }
  .agent__title { color: var(--muted); font-size: 11px; margin-top: 3px; }

  .agent-photo {
    position: absolute; left: 376px; top: 68px;
    width: 156px; height: 190px;
    background: linear-gradient(180deg, #d9d9d9 0%, #b9b0a8 45%, #3a3a3a 100%);
  }
  .badges {
    position: absolute; left: 24px; top: 114px;
    display: flex; gap: 10px; align-items: center;
  }
  .badge { background: var(--badge); }
  .badge--office { width: 42px; height: 26px; border-radius: 2px; }
  .badge--realtor { width: 24px; height: 24px; }
  .badge--listing { width: 36px; height: 24px; border-radius: 2px; }

  .contacts {
    position: absolute; left: 24px; top: 160px;
    list-style: none;
    font-size: 12px;
    color: var(--ink);
  }
  .contacts li { display: flex; align-items: center; gap: 7px; height: 23px; }
  .contacts svg { width: 11px; height: 11px; fill: var(--gold); flex: none; }

  .swoosh { position: absolute; left: 0; top: 236px; width: 532px; height: 100px; }
  .address {
    position: absolute; left: 28px; top: 288px;
    color: #fff; font-size: 12px;
  }

  .card--back .brand {
    position: absolute; left: 0; right: 0; top: 112px;
    justify-content: center;
    font-size: 34px;
  }
  .disclaimer {
    position: absolute; left: 0; right: 0; top: 206px;
    text-align: center; font-size: 12px; color: var(--ink);
  }
  .website {
    position: absolute; left: 0; right: 0; top: 246px;
    text-align: center; font-size: 12px; letter-spacing: 2px;
    color: var(--brand-red);
  }
</style>
</head>
<body>
  <section class="card card--front">
    <div class="brand"><span class="brand__mark"></span>Lena Vortham Realty</div>

    <div class="agent">
      <div class="agent__name">Lena Vortham</div>
      <div class="agent__title">Realtor</div>
    </div>

    <div class="badges">
      <div class="badge badge--office" aria-label="Dunmore Pike office badge"></div>
      <div class="badge badge--realtor" aria-label="Realtor badge"></div>
      <div class="badge badge--listing" aria-label="HPX listing badge"></div>
    </div>

    <ul class="contacts">
      <li><svg viewBox="0 0 12 12"><path d="M2.5 0.5l2 2.5-1.2 1.3a7 7 0 0 0 4.4 4.4L9 7.5l2.5 2-1 2C5 11.5 0.5 7 0.5 1.5z"/></svg>555-014-2738</li>
      <li><svg viewBox="0 0 12 12"><path d="M0 2h12v8H0zM0.8 2.6L6 6.6l5.2-4z" fill-rule="evenodd"/></svg>Lena@LenaVorthamRealty.example</li>
      <li><svg viewBox="0 0 12 12"><circle cx="6" cy="6" r="5.5"/></svg>www.LenaVorthamRealty.example</li>
    </ul>

    <div class="agent-photo" role="img" aria-label="Portrait photograph of the agent"></div>

    <svg class="swoosh" viewBox="0 0 532 100" preserveAspectRatio="none">
      <path d="M0 24 C150 8 330 26 532 10 L532 100 L0 100 Z" fill="var(--gold)"/>
      <path d="M0 30 C160 16 330 32 532 18 L532 100 L0 100 Z" fill="var(--band)"/>
    </svg>
    <div class="address">4817 Bellgrove Lane, Ste. 300 Allen, TX 75098</div>
  </section>

  <section class="card card--back">
    <div class="brand"><span class="brand__mark"></span>Lena Vortham Realty</div>
    <p class="disclaimer">Each Dunmore Pike Office is Independently owned &amp; Operated.</p>
    <p class="website">www.LenaVorthamRealty.example</p>
  </section>
</body>
</html>
```